Buchungsplattform für Hypnose-Dienstleistungen sucht Zertifikat-Design
Zielgruppe
Buchungsplattform für Hypnose Dienstleistungen. Die Zielgruppe des angeklagten Design (Zertifikat) geht an registrierte Anbieter (Hypnosetherapeuten, Praxes, Zahnärzte, etc).
Aufgabenstellung
Das gewünschte Zertifikat soll;
- unser CI/CD berücksichtigen (Primär Orange: #DD3200 Sekundär Blau: #0085A8(
- soll einen wertvollen, aufwendigen, besonderen Eindruck vermitteln
- soll sich inhaltlich in etwa dem angehängten Vorschlag orientieren
- kann spezielle Druckverfahren (Prägedruck, Stanz, Laser, etc. ) in Erwägung ziehen wo angebracht

```html
<!DOCTYPE html>
<html lang="de">
<head>
<meta charset="utf-8">
<title>Certificate of Excellence – Somnara</title>
<link href="https://fonts.googleapis.com/css2?family=Crimson+Pro:wght@400;700&display=swap" rel="stylesheet">
<style>
  :root {
    --orange: #dd3200;
    --blue: #0a68a0;
    --ink: #111111;
    --paper: #ffffff;
    --wave-tint: rgba(242, 165, 140, 0.28);
  }
  html, body { margin: 0; padding: 0; overflow: hidden; }
  body { width: 848px; height: 1200px; background: var(--paper); }
  .certificate {
    position: relative;
    width: 848px;
    height: 1200px;
    overflow: hidden;
    background: var(--paper);
    font-family: "Crimson Pro", "Times New Roman", serif;
    color: var(--ink);
  }
  .decor-band {
    position: absolute; left: 0; top: 850px; width: 848px; height: 350px;
    background: linear-gradient(180deg, transparent 0%, var(--wave-tint) 100%);
  }
  .brand-name {
    position: absolute; top: 52px; left: 0; width: 100%;
    text-align: center; margin: 0;
    font-size: 84px; font-weight: 400; letter-spacing: 6px;
    line-height: 1; color: var(--orange);
  }
  .title {
    position: absolute; top: 256px; left: 0; width: 100%;
    text-align: center; margin: 0;
    font-size: 76px; font-weight: 700; line-height: 78px;
    color: var(--blue); letter-spacing: 1px;
  }
  .practice-name {
    position: absolute; top: 494px; left: 0; width: 100%;
    text-align: center; margin: 0;
    font-size: 66px; font-weight: 400; line-height: 1;
  }
  .rule {
    position: absolute; height: 1.5px;
    background: linear-gradient(90deg, transparent, var(--orange) 20%, var(--orange) 80%, transparent);
  }
  .rule-main { top: 573px; left: 175px; width: 498px; }
  .holder {
    position: absolute; top: 592px; left: 0; width: 100%;
    text-align: center; margin: 0;
    font-size: 25px; line-height: 29px; text-transform: uppercase;
  }
  .statement {
    position: absolute; top: 675px; left: 0; width: 100%;
    text-align: center; margin: 0;
    font-size: 40px; line-height: 45px;
  }
  .signature { position: absolute; top: 901px; width: 265px; }
  .signature .rule { position: static; width: 100%; }
  .signature p {
    margin: 9px 0 0 31px;
    font-size: 22.5px; line-height: 24px; text-transform: uppercase;
    white-space: nowrap;
  }
  .signature-left { left: 68px; }
  .signature-right { left: 495px; }
</style>
</head>
<body>
<main class="certificate">
  <div class="decor-band" role="img" aria-label="Dekoratives Band aus feinen, geschwungenen orangefarbenen Linien"></div>

  <h1 class="brand-name">SOMNARA</h1>

  <h2 class="title">CERTIFICATE<br>OF EXCELLENCE</h2>

  <p class="practice-name">Praxisname</p>
  <div class="rule rule-main"></div>

  <p class="holder">Vorname&nbsp; Nachname<br>Adresse&nbsp;&nbsp; / &nbsp;&nbsp;PLZ Ort</p>

  <p class="statement">wird für seine hervorragende Qualität<br>und Betriebsleistung anerkannt.</p>

  <div class="signature signature-left">
    <div class="rule"></div>
    <p>Somnara Schweiz AG<br>Quality Assurance</p>
  </div>
  <div class="signature signature-right">
    <div class="rule"></div>
    <p>Somnara Schweiz AG<br>Quality Assurance</p>
  </div>
</main>
</body>
</html>
```